Brightvale Fluid Systems Corp Business Cards

Business cards to match the logo.

Company is a start up water technology company that has developed a patented system using centrifugal force to separate waste from municipal waste water to produce crystal clear clean water. Product sell starting at 2 million to governments both in the US and international.

Business cards should have a professional look with the target generally engineers.

Target Market(s)

Engineers, Government officials and investors

Industry/Entity Type

Water Treatment

Contact Information for Business Card

Business cards design will be used for 6 to 8 people with job titles. Can use the quote "If there is magic in the planet, it is contained in water." but not required to use quote. Should follow theme of Logo

Font styles to use
Other font styles liked:
• match logo font

Requirements
Nice to have
• Colors to match Logo. Business cards to match style of flow of Logo.
• Emphasis on clean look not a busy look. Clean flowing water.
Should not have
• Pictures of industrial equipment or wastewater

```html
<!DOCTYPE html>
<html lang="en">
<head>
<meta charset="utf-8">
<title>Brightvale Fluid Systems — Business Cards</title>
<link href="https://fonts.googleapis.com/css2?family=Playfair+Display:wght@400;500&display=swap" rel="stylesheet">
<style>
  :root {
    --page: #e4e6e8;
    --blue-bright: #2ba8e0;
    --blue-mid: #1f8dc7;
    --blue-deep: #176a9f;
    --blue-night: #135e8f;
    --white: #ffffff;
    --shadow: rgba(20, 40, 60, 0.28);
  }
  * { margin: 0; padding: 0; box-sizing: border-box; }
  html, body {
    width: 1200px; height: 900px; overflow: hidden;
    background: var(--page);
    font-family: "Playfair Display", Georgia, serif;
  }
  .sheet {
    position: relative; width: 1200px; height: 900px;
  }
  .card {
    position: absolute; left: 290px;
    width: 620px; height: 354px;
    overflow: hidden;
    box-shadow: 0 14px 30px var(--shadow);
    color: var(--white);
  }
  .card--back { top: 62px; }
  .card--front { top: 484px; }
  .card__art { position: absolute; inset: 0; width: 100%; height: 100%; }

  /* front */
  .wordmark {
    position: absolute; right: 44px; top: 128px;
    text-align: right;
    font-weight: 400; font-size: 40px; line-height: 1.1;
    letter-spacing: 2px; text-transform: uppercase;
    color: var(--white);
  }

  /* back */
  .wordmark--small {
    position: absolute; left: 38px; top: 26px;
    font-weight: 400; font-size: 13px; line-height: 1.2;
    letter-spacing: 1.5px; text-transform: uppercase;
    color: var(--white);
  }
  .holder {
    position: absolute; left: 38px; top: 112px;
    text-transform: uppercase;
  }
  .holder__name { font-size: 22px; font-weight: 500; letter-spacing: 0.5px; }
  .holder__title { font-size: 16px; font-weight: 400; margin-top: 2px; letter-spacing: 0.5px; }

  .contacts {
    position: absolute; left: 320px; top: 124px;
    list-style: none;
    font-size: 15px; line-height: 1;
  }
  .contacts__item {
    display: flex; align-items: center; gap: 10px;
    height: 28px;
  }
  .contacts__icon { width: 16px; height: 16px; flex: none; }
</style>
</head>
<body>
<main class="sheet">

  <section class="card card--back" aria-label="Business card back">
    <svg class="card__art" viewBox="0 0 620 354" aria-hidden="true">
      <defs>
        <linearGradient id="backBase" x1="0" y1="0" x2="1" y2="1">
          <stop offset="0" stop-color="#1d86c0"/>
          <stop offset="1" stop-color="#145f90"/>
        </linearGradient>
        <radialGradient id="backDisc" cx="0.55" cy="0.35" r="0.7">
          <stop offset="0" stop-color="#33b0e6"/>
          <stop offset="1" stop-color="#1f88c2"/>
        </radialGradient>
      </defs>
      <rect width="620" height="354" fill="url(#backBase)"/>
      <circle cx="450" cy="120" r="280" fill="url(#backDisc)"/>
      <path d="M0 0 H240 C170 60 150 170 210 354 H0 Z" fill="#1b7db6" opacity="0.55"/>
    </svg>

    <p class="wordmark--small">Brightvale Fluid<br>Systems</p>

    <div class="holder">
      <p class="holder__name">Your Name Here</p>
      <p class="holder__title">Your Title Here</p>
    </div>

    <ul class="contacts">
      <li class="contacts__item">
        <svg class="contacts__icon" viewBox="0 0 16 16" aria-hidden="true"><path d="M8 1a5 5 0 0 0-5 5c0 4 5 9 5 9s5-5 5-9a5 5 0 0 0-5-5zm0 7a2 2 0 1 1 0-4 2 2 0 0 1 0 4z" fill="#fff"/></svg>
        Company address here
      </li>
      <li class="contacts__item">
        <svg class="contacts__icon" viewBox="0 0 16 16" aria-hidden="true"><path d="M4 1.5l2.2 3-1.3 1.6a8 8 0 0 0 5 5l1.6-1.3 3 2.2-1.4 2.5C7.7 14 2 8.3 1.5 2.9z" fill="#fff"/></svg>
        Company phone number
      </li>
      <li class="contacts__item">
        <svg class="contacts__icon" viewBox="0 0 16 16" aria-hidden="true"><rect x="4" y="1" width="8" height="14" rx="1.5" fill="#fff"/><rect x="5.5" y="3" width="5" height="7" fill="#1f88c2"/><circle cx="8" cy="12.5" r="1" fill="#1f88c2"/></svg>
        Cell phone number
      </li>
      <li class="contacts__item">
        <svg class="contacts__icon" viewBox="0 0 16 16" aria-hidden="true"><rect x="1" y="3" width="14" height="10" fill="#fff"/><path d="M1 3l7 6 7-6" fill="none" stroke="#1f88c2" stroke-width="1.3"/></svg>
        e-mail address
      </li>
      <li class="contacts__item">
        <svg class="contacts__icon" viewBox="0 0 16 16" aria-hidden="true"><circle cx="8" cy="8" r="6.5" fill="none" stroke="#fff" stroke-width="1.4"/><ellipse cx="8" cy="8" rx="2.8" ry="6.5" fill="none" stroke="#fff" stroke-width="1.2"/><path d="M1.5 8h13M2.5 4.8h11M2.5 11.2h11" stroke="#fff" stroke-width="1.1"/></svg>
        Web-site address
      </li>
    </ul>
  </section>

  <section class="card card--front" aria-label="Business card front">
    <svg class="card__art" viewBox="0 0 620 354" aria-hidden="true">
      <defs>
        <linearGradient id="frontBase" x1="0" y1="0" x2="1" y2="1">
          <stop offset="0" stop-color="#2fadE4"/>
          <stop offset="1" stop-color="#2192cc"/>
        </linearGradient>
        <linearGradient id="frontOval" x1="0" y1="0" x2="1" y2="0">
          <stop offset="0" stop-color="#155f91"/>
          <stop offset="0.55" stop-color="#1d7fb8"/>
          <stop offset="1" stop-color="#2aa3dc"/>
        </linearGradient>
      </defs>
      <rect width="620" height="354" fill="url(#frontBase)"/>
      <ellipse cx="470" cy="150" rx="360" ry="120" fill="url(#frontOval)"/>
      <path d="M0 250 C160 300 380 320 620 290 L620 354 L0 354 Z" fill="#2398d2"/>
      <path d="M0 290 C180 320 420 340 620 318 L620 354 L0 354 Z" fill="#1c82bc"/>
      <path d="M0 322 C220 340 440 350 620 340 L620 354 L0 354 Z" fill="#176fa5"/>
    </svg>

    <p class="wordmark">Brightvale Fluid<br>Systems</p>
  </section>

</main>
</body>
</html>
```